Icon tabs required for Hosting/Telco company

We have a project underway to launch a new online services catalogue for our customers. We have a draft screen (one of the attachments), but we have decided to extend the services catalogue to all our lines of business:

- network (data network/WAN services)
- hosting (cloud servers etc.)
- voice (telephones etc.)
- mobiles (mobile phones)

and now the tabs we have added ourselves look poor. We would like four tabs (on and off state) developed to replace the standard JQuery tabs currently in use. They need to fit into the existing draft user interface in progress.

Target Market(s)

Business customers, educated, typically IT Professionals.

Industry/Entity Type

It Company

Requirements
Should not have
• Should not require us to change the rest of the screen too much. We can move the existing Product/Application tabs to the right a little bit, but if the tabs are too big they will not fit.

```html
<!DOCTYPE html>
<html lang="en">
<head>
<meta charset="utf-8">
<title>Service Catalogue Tabs</title>
<link rel="stylesheet" href="https://fonts.googleapis.com/css2?family=Arimo:wght@400;700&display=swap">
<style>
:root{
  --page:#ffffff;
  --ink:#222222;
  --muted:#666666;
  --line:#c9ced6;
  --tab-top:#ffffff;
  --tab-bottom:#e6e9ee;
  --active-top:#39b6ef;
  --active-bottom:#0a84cf;
  --link:#1a6fc4;
  --side-top:#d9ecf9;
  --side-bottom:#9fcdee;
  --side-icon:#1f6fb3;
  --head:#eceff3;
  --row-icon:#b9bfc8;
}
*{box-sizing:border-box;margin:0;padding:0}
html,body{width:841px;height:1200px;overflow:hidden;background:var(--page)}
body{position:relative;font-family:"Arimo",Arial,sans-serif;color:var(--ink)}
svg.defs{position:absolute;width:0;height:0}

.tabset{position:absolute;display:flex;gap:6px}
.tabset.large{left:222px}
.tab{display:flex;align-items:center;gap:8px;height:44px;padding:0 16px;border:1px solid var(--line);border-radius:4px;
  background:linear-gradient(var(--tab-top),var(--tab-bottom));font-size:17px;color:var(--ink);white-space:nowrap}
.tab svg{width:22px;height:22px;fill:currentColor}
.tab.active{background:linear-gradient(var(--active-top),var(--active-bottom));color:#fff;border-color:#0a75b8}
.tabset.alt .tab{border-radius:2px;box-shadow:0 1px 2px rgba(0,0,0,.2)}

.screen{position:absolute;left:30px;width:811px;height:540px;overflow:hidden}
.screen .tabset{left:12px;top:2px;gap:3px}
.screen .tab{height:32px;padding:0 9px;font-size:13px;gap:5px;border-radius:3px}
.screen .tab svg{width:16px;height:16px}
.viewtabs{position:absolute;left:395px;top:2px;display:flex;gap:6px}
.viewtab{height:36px;padding:0 22px;border:1px solid var(--line);border-bottom:none;border-radius:5px 5px 0 0;
  background:#f2f4f7;color:var(--link);font-size:15px;line-height:36px;white-space:nowrap}
.viewtab.current{background:#fff}
.frame{position:absolute;left:0;top:38px;right:0;bottom:0;border-top:1px solid var(--line)}

.sidebar{position:absolute;left:12px;top:8px;width:198px;bottom:0;
  background:linear-gradient(90deg,var(--side-top),var(--side-bottom));border-radius:4px 0 0 0}
.side-item{display:flex;align-items:center;gap:14px;height:74px;padding-left:12px;font-size:15px;color:var(--ink)}
.side-item.current{background:#fff;border:1px solid var(--line);border-right:none;margin-right:-1px}
.side-icon{width:42px;height:42px;border-radius:50%;background:var(--side-icon);border:3px solid #fff;
  display:flex;align-items:center;justify-content:center;flex:none}
.side-icon svg{width:20px;height:20px;fill:#fff}

.content{position:absolute;left:225px;top:20px;right:0;bottom:0}
.pager{position:absolute;left:10px;top:6px;display:flex;gap:10px;align-items:center;font-size:14px}
.pager .box{border:1px solid var(--line);padding:3px 7px;border-radius:3px}
.search{position:absolute;left:290px;top:0;width:235px;height:34px;border:1px solid var(--line);border-radius:3px;
  padding:0 10px;line-height:32px;font-size:15px}
.search svg{position:absolute;right:8px;top:7px;width:18px;height:18px;stroke:var(--side-icon);fill:none;stroke-width:2.5}
.cut{position:absolute;left:545px;top:8px;color:var(--link);font-size:15px;font-weight:700}

.grid{position:absolute;left:0;top:62px;right:0}
.grid-head{display:flex;height:28px;background:var(--head);border:1px solid var(--line);font-size:14px;line-height:26px}
.grid-head span{padding-left:10px}
.col-type{width:225px}
.col-name{width:220px}
.row{display:flex;height:78px;border-bottom:1px solid #e1e4e9;font-size:13px;padding-top:8px}
.row .col-type{display:flex;gap:8px;padding-left:10px;padding-right:40px;color:var(--muted);line-height:16px}
.row-icon{width:30px;height:30px;background:var(--row-icon);border-radius:3px;flex:none}
.row .col-name{padding-left:10px;line-height:17px;color:var(--muted)}
.row .col-name b{display:block;color:var(--link)}
.row .col-set{padding-left:10px;line-height:17px}
</style>
</head>
<body>
<svg class="defs" aria-hidden="true">
  <symbol id="i-network" viewBox="0 0 24 24"><rect x="9" y="2" width="6" height="5"/><rect x="2" y="16" width="6" height="5"/><rect x="16" y="16" width="6" height="5"/><rect x="11.2" y="7" width="1.6" height="5"/><rect x="4.2" y="11" width="15.6" height="1.6"/><rect x="4.2" y="11" width="1.6" height="5"/><rect x="18.2" y="11" width="1.6" height="5"/></symbol>
  <symbol id="i-hosting" viewBox="0 0 24 24"><rect x="3" y="3" width="18" height="5" rx="1"/><rect x="3" y="10" width="18" height="5" rx="1"/><rect x="3" y="17" width="18" height="5" rx="1"/></symbol>
  <symbol id="i-mobile" viewBox="0 0 24 24"><path d="M7 1h10a1 1 0 0 1 1 1v20a1 1 0 0 1-1 1H7a1 1 0 0 1-1-1V2a1 1 0 0 1 1-1zm1 3v14h8V4z"/></symbol>
  <symbol id="i-voice" viewBox="0 0 24 24"><path d="M2 8c0-3 4-5 10-5s10 2 10 5v2h-5V8H7v2H2z"/><path d="M6 12h12l3 9H3z"/></symbol>
  <symbol id="i-compute" viewBox="0 0 24 24"><rect x="3" y="4" width="18" height="12" rx="1"/><rect x="9" y="17" width="6" height="3"/></symbol>
  <symbol id="i-storage" viewBox="0 0 24 24"><ellipse cx="12" cy="5" rx="8" ry="3"/><path d="M4 7v12c0 2 4 3 8 3s8-1 8-3V7c0 2-4 3-8 3S4 9 4 7z"/></symbol>
  <symbol id="i-colo" viewBox="0 0 24 24"><rect x="5" y="2" width="14" height="20" rx="1"/></symbol>
  <symbol id="i-other" viewBox="0 0 24 24"><circle cx="5" cy="12" r="2.5"/><circle cx="12" cy="12" r="2.5"/><circle cx="19" cy="12" r="2.5"/></symbol>
</svg>

<nav class="tabset large" style="top:42px">
  <span class="tab"><svg><use href="#i-network"/></svg>Network</span>
  <span class="tab active"><svg><use href="#i-hosting"/></svg>Hosting</span>
  <span class="tab"><svg><use href="#i-mobile"/></svg>Mobile</span>
  <span class="tab"><svg><use href="#i-voice"/></svg>Voice</span>
</nav>
<nav class="tabset large alt" style="top:126px">
  <span class="tab"><svg><use href="#i-network"/></svg>Network</span>
  <span class="tab active"><svg><use href="#i-hosting"/></svg>Hosting</span>
  <span class="tab"><svg><use href="#i-mobile"/></svg>Mobile</span>
  <span class="tab"><svg><use href="#i-voice"/></svg>Voice</span>
</nav>

<section class="screen" style="top:200px">
  <nav class="tabset">
    <span class="tab"><svg><use href="#i-network"/></svg>Network</span>
    <span class="tab active"><svg><use href="#i-hosting"/></svg>Hosting</span>
    <span class="tab"><svg><use href="#i-mobile"/></svg>Mobile</span>
    <span class="tab"><svg><use href="#i-voice"/></svg>Voice</span>
  </nav>
  <div class="viewtabs"><span class="viewtab current">Product View ☰</span><span class="viewtab">Application View ▦</span></div>
  <div class="frame">
    <aside class="sidebar">
      <div class="side-item current"><span class="side-icon"><svg><use href="#i-compute"/></svg></span>Compute</div>
      <div class="side-item"><span class="side-icon"><svg><use href="#i-network"/></svg></span>Network</div>
      <div class="side-item"><span class="side-icon"><svg><use href="#i-storage"/></svg></span>Storage</div>
      <div class="side-item"><span class="side-icon"><svg><use href="#i-colo"/></svg></span>Co-location</div>
      <div class="side-item"><span class="side-icon"><svg><use href="#i-other"/></svg></span>Other</div>
    </aside>
    <div class="content">
      <div class="pager">1 to 50 of 55 <span class="box">1</span><span class="box">2</span>… ▸</div>
      <div class="search">NTCPS<svg viewBox="0 0 20 20"><circle cx="8" cy="8" r="6"/><path d="M12.5 12.5L18 18"/></svg></div>
      <div class="cut">De</div>
      <div class="grid">
        <div class="grid-head"><span class="col-type">Service Type ▾</span><span class="col-name">Service Name ▾</span><span>Settings ▾</span></div>
        <div class="row"><div class="col-type"><span class="row-icon"></span>Northgate Telecom Cloud Performance Server</div><div class="col-name"><b>Cloud Performance Server : CPS - CRS...</b>NTCPS25956007</div><div class="col-set">4 CPU / 16GB RAM<br>gsv82-Entx64</div></div>
        <div class="row"><div class="col-type"><span class="row-icon"></span>Northgate Telecom Cloud Performance Server</div><div class="col-name"><b>CPS - NTVMEXM01 - 2445GB</b>NTCPS21473002</div><div class="col-set">4 CPU / 8GB RAM<br>gsv82-Stdx64</div></div>
        <div class="row"><div class="col-type"><span class="row-icon"></span>Northgate Telecom Cloud Performance Server</div><div class="col-name"><b>Cloud Performance Server : CPS - NTVM...</b>NTCPS21473001</div><div class="col-set">4 CPU / 8GB RAM<br>gsv82-Stdx64</div></div>
        <div class="row"><div class="col-type"><span class="row-icon"></span>Northgate Telecom Cloud Performance Server</div><div class="col-name"><b>Cloud Performance Server : CPS - LDAP...</b>NTCPS25956002</div><div class="col-set">4 CPU / 8GB RAM<br>gsv82-Entx64</div></div>
      </div>
    </div>
  </div>
</section>

<section class="screen" style="top:760px">
  <nav class="tabset alt">
    <span class="tab"><svg><use href="#i-network"/></svg>Network</span>
    <span class="tab active"><svg><use href="#i-hosting"/></svg>Hosting</span>
    <span class="tab"><svg><use href="#i-mobile"/></svg>Mobile</span>
    <span class="tab"><svg><use href="#i-voice"/></svg>Voice</span>
  </nav>
  <div class="viewtabs"><span class="viewtab current">Product View ☰</span><span class="viewtab">Application View ▦</span></div>
  <div class="frame">
    <aside class="sidebar">
      <div class="side-item current"><span class="side-icon"><svg><use href="#i-compute"/></svg></span>Compute</div>
      <div class="side-item"><span class="side-icon"><svg><use href="#i-network"/></svg></span>Network</div>
      <div class="side-item"><span class="side-icon"><svg><use href="#i-storage"/></svg></span>Storage</div>
      <div class="side-item"><span class="side-icon"><svg><use href="#i-colo"/></svg></span>Co-location</div>
      <div class="side-item"><span class="side-icon"><svg><use href="#i-other"/></svg></span>Other</div>
    </aside>
    <div class="content">
      <div class="pager">1 to 50 of 55 <span class="box">1</span><span class="box">2</span>… ▸</div>
      <div class="search">NTCPS<svg viewBox="0 0 20 20"><circle cx="8" cy="8" r="6"/><path d="M12.5 12.5L18 18"/></svg></div>
      <div class="cut">De</div>
      <div class="grid">
        <div class="grid-head"><span class="col-type">Service Type ▾</span><span class="col-name">Service Name ▾</span><span>Settings ▾</span></div>
        <div class="row"><div class="col-type"><span class="row-icon"></span>Northgate Telecom Cloud Performance Server</div><div class="col-name"><b>Cloud Performance Server : CPS - CRS...</b>NTCPS25956007</div><div class="col-set">4 CPU / 16GB RAM<br>gsv82-Entx64</div></div>
        <div class="row"><div class="col-type"><span class="row-icon"></span>Northgate Telecom Cloud Performance Server</div><div class="col-name"><b>CPS - NTVMEXM01 - 2445GB</b>NTCPS21473002</div><div class="col-set">4 CPU / 8GB RAM<br>gsv82-Stdx64</div></div>
        <div class="row"><div class="col-type"><span class="row-icon"></span>Northgate Telecom Cloud Performance Server</div><div class="col-name"><b>Cloud Performance Server : CPS - NTVM...</b>NTCPS21473001</div><div class="col-set">4 CPU / 8GB RAM<br>gsv82-Stdx64</div></div>
        <div class="row"><div class="col-type"><span class="row-icon"></span>Northgate Telecom Cloud Performance Server</div><div class="col-name"><b>Cloud Performance Server : CPS - LDAP...</b>NTCPS25956002</div><div class="col-set">4 CPU / 8GB RAM<br>gsv82-Entx64</div></div>
      </div>
    </div>
  </div>
</section>
</body>
</html>
```